Halvoran Books & Consulting Brochure

I need a double sided brochure for a small business bookkeeping & consulting firm.

Halvoran Books & Consulting (I have attached the Logo)

The brochure will be printed on 8.5" x 5.5" paper (Pif).

I'd like to use blues, whites and black colors...

The final product needs to communicate security, professional and current (not futuristic or dated).

I wouldn't mind a picture on 1 of the sides (professional person, a professional meeting, something along those lines).

I am visioning the brochure having 4 sections (2 on front and 2 on back)

Section 1 - Why Outsource Bookkeeping?
Section 2 - Our Philosophy
Section 3 - Services
Section 4 - TBD

I'd like a shell to review before deciding on all of the wording. Some wording is below:

Why Outsource Bookkeeping?

More Time to Focus on your core business
2) Save Money – No More: payroll taxes, workers compensation, benefits, vacation, sick days, office space, hardware, technology, training, turnover…
3) Expertise – you have full time access to a highly skilled team at the cost of a paying a part time bookkeeper.
4) Focused Staff – no more office distractions. Having a remote bookkeeper allows you to focus on your business and allows them to focus on your financials.
5) Access to Top Technology Systems –outsourcing gives you access to the top tool in the industry. You don’t have the time to research and learn about the best financial tools for your business – let an expert handle that
6) Experience – an outsourced bookkeeper can share relevant knowledge gained from experience with other clients

Services:
Bookkeeping Controller Services Accounts Payable Management
Account Receivable Management Check Writing Account Reconciliations
Benchmarking Budgeting Financial Reports
Financial Consulting Profit and Growth Consulting Financial Planning
Succession & Exit Planning Electronic Filing Cabinet Marketing Consulting

Our Philosophy:

Accuracy – having strong financial systems in place that collect and measure all relevant data creates a compliant business and gives you a better understanding of your business.
Understanding – Understanding what financial data is important and what it really means for your business will allow you to take appropriate actions to grow your business or to prevent future issues.
Action – data in meaningless without action, however the right actions put you in control
Control – When you take action based on accurate data that you understand, you are in complete control of your business and its future.

Industry/Entity Type

Small Business

```html
<!DOCTYPE html>
<html lang="en">
<head>
<meta charset="utf-8">
<title>Halvoran Books &amp; Consulting – Brochure</title>
<link href="https://fonts.googleapis.com/css2?family=Titillium+Web:wght@300;400;600;700&display=swap" rel="stylesheet">
<style>
  :root{
    --paper:#ffffff;
    --dark-top:#3b3c3e;
    --dark-bottom:#161718;
    --ink:#2b2c2e;
    --blue:#1c8cc4;
    --blue-deep:#17628f;
    --blue-bright:#2aa9e1;
    --text-light:#d2d2d2;
    --text-white:#ffffff;
    --icon:#a9a9a9;
  }
  *{box-sizing:border-box;margin:0;padding:0}
  html,body{width:1200px;height:899px;overflow:hidden;background:var(--paper)}
  body{position:relative;font-family:"Titillium Web",Arial,sans-serif}

  .panel{position:absolute;top:0;height:899px;overflow:hidden;
    background:linear-gradient(180deg,var(--dark-top) 0%,#262728 55%,var(--dark-bottom) 100%)}
  .panel--front{left:0;width:580px}
  .panel--back{left:625px;width:575px}
  .panel-shapes{position:absolute;inset:0;width:100%;height:100%}

  /* front */
  .meeting-photo{position:absolute;left:0;top:0;width:580px;height:400px;
    background:linear-gradient(120deg,#dfe7ec 0%,#b9c7d1 35%,#5d6f80 60%,#2c3440 85%,#1d2530 100%)}
  .section-title{position:absolute;color:var(--text-white);font-weight:600;font-size:25px;letter-spacing:.3px;line-height:1}
  .front-title{left:108px;top:388px}
  .reasons{position:absolute;left:0;top:0;list-style:none}
  .reason{position:absolute;left:108px;width:445px;color:var(--text-light);font-weight:300;
    font-size:12px;line-height:15.6px;text-align:justify}
  .reason-icon{position:absolute;left:-65px;width:40px;height:40px}
  .reason-icon svg{width:40px;height:40px}

  /* back */
  .round-frame{position:absolute;width:156px;height:156px;border-radius:50%;
    background:radial-gradient(circle at 35% 30%,#ffffff 0%,#e7e7e7 60%,#bdbdbd 100%);
    box-shadow:0 10px 18px rgba(0,0,0,.55)}
  .round-frame .round-photo{position:absolute;left:15px;top:15px;width:126px;height:126px;border-radius:50%}
  .frame-services{left:39px;top:130px}
  .frame-philosophy{left:39px;top:430px}
  .photo-team{background:linear-gradient(135deg,#e3e8ec 0%,#9fb1c0 45%,#3e4f63 80%,#26303c 100%)}
  .photo-growth{background:radial-gradient(circle at 50% 60%,#5fb9e6 0%,#1e6c9e 45%,#0f2f4c 100%)}

  .back-title{left:230px}
  .services-title{top:115px}
  .philosophy-title{top:371px}
  .copy{position:absolute;left:230px;width:323px;color:var(--text-light);font-weight:300;
    font-size:12.4px;line-height:15.6px;text-align:justify}
  .services-list{top:144px;list-style:none}
  .philosophy-copy{top:416px}

  .contact{position:absolute;left:232px;top:652px;list-style:none;color:var(--blue-bright);font-weight:600;font-size:14.5px;line-height:19.5px}
  .contact li{display:flex;align-items:center;gap:4px}
  .contact svg{width:12px;height:12px;fill:#e6e6e6}

  .web-address{position:absolute;left:23px;top:840px;color:var(--text-white);font-weight:300;font-size:27px;letter-spacing:.5px}

  /* name in corner tile */
  .corner-tile{position:absolute;width:170px;height:170px;background:var(--paper);border-radius:22px;transform:rotate(45deg)}
  .panel--front .corner-tile{left:450px;top:795px}
  .panel--back .corner-tile{left:405px;top:765px}
  .name-mark{position:absolute;color:var(--ink);font-weight:600;font-size:22px;line-height:1}
  .panel--front .name-mark{left:470px;top:856px}
  .panel--back .name-mark{left:445px;top:838px}
</style>
</head>
<body>

<section class="panel panel--front">
  <div class="meeting-photo" role="img" aria-label="Photo of a professional business meeting around a table"></div>
  <svg class="panel-shapes" viewBox="0 0 580 899" aria-hidden="true">
    <defs>
      <linearGradient id="darkFront" x1="0" y1="0" x2="0" y2="1">
        <stop offset="0" stop-color="#3b3c3e"/><stop offset=".5" stop-color="#262728"/><stop offset="1" stop-color="#161718"/>
      </linearGradient>
    </defs>
    <path d="M0 330 Q300 278 580 318 L580 899 L0 899Z" fill="#ffffff"/>
    <path d="M0 342 Q300 290 580 326 L580 899 L0 899Z" fill="var(--blue)"/>
    <path d="M0 392 Q290 318 580 362 L580 899 L0 899Z" fill="url(#darkFront)"/>
  </svg>

  <h2 class="section-title front-title">Why Outsource Bookkeeping?</h2>

  <ul class="reasons">
    <li class="reason" style="top:434px">
      <span class="reason-icon" style="top:-13px"><svg viewBox="0 0 40 40" fill="none" stroke="var(--icon)" stroke-width="2"><circle cx="20" cy="20" r="12"/><circle cx="20" cy="20" r="5"/><path d="M20 2v10M20 28v10M2 20h10M28 20h10"/></svg></span>
      More Time to Focus on your core business
    </li>
    <li class="reason" style="top:481px">
      <span class="reason-icon" style="top:-4px"><svg viewBox="0 0 40 40" fill="var(--icon)"><ellipse cx="20" cy="22" rx="14" ry="11"/><circle cx="27" cy="9" r="4"/><rect x="10" y="30" width="5" height="7"/><rect x="24" y="30" width="5" height="7"/></svg></span>
      Save Money – No More: payroll taxes, workers compensation, benefits, vacation, sick days, office space, hardware, technology, training, turnover…
    </li>
    <li class="reason" style="top:541px">
      <span class="reason-icon" style="top:-6px"><svg viewBox="0 0 40 40" fill="var(--icon)"><circle cx="20" cy="7" r="4"/><rect x="15" y="12" width="10" height="24" rx="2"/><circle cx="9" cy="10" r="3.5"/><rect x="5" y="15" width="8" height="18" rx="2"/><circle cx="31" cy="10" r="3.5"/><rect x="27" y="15" width="8" height="18" rx="2"/></svg></span>
      Expertise – you have full time access to a highly skilled team at the cost of a paying a part time bookkeeper.
    </li>
    <li class="reason" style="top:606px">
      <span class="reason-icon" style="top:-6px"><svg viewBox="0 0 40 40" fill="var(--icon)"><circle cx="12" cy="12" r="6"/><path d="M1 32 Q12 16 23 32Z"/><circle cx="28" cy="12" r="6"/><path d="M17 32 Q28 16 39 32Z"/></svg></span>
      Focused Staff – no more office distractions. Having a remote bookkeeper allows you to focus on your business and allows them to focus on your financials.
    </li>
    <li class="reason" style="top:683px">
      <span class="reason-icon" style="top:-8px"><svg viewBox="0 0 40 40" fill="none" stroke="var(--icon)" stroke-width="2.4"><rect x="9" y="3" width="22" height="34" rx="3"/><path d="M14 10h12M14 16h12M14 22h8"/></svg></span>
      Access to Top Technology Systems –outsourcing gives you access to the top tool in the industry. You don’t have the time to research and learn about the best financial tools for your business – let an expert handle that
    </li>
    <li class="reason" style="top:759px">
      <span class="reason-icon" style="top:-14px"><svg viewBox="0 0 40 40" fill="var(--icon)"><circle cx="11" cy="9" r="5"/><circle cx="29" cy="9" r="5"/><path d="M3 34 V20 Q3 15 10 15 L20 24 L30 15 Q37 15 37 20 V34 Z"/></svg></span>
      Experience – an outsourced bookkeeper can share relevant knowledge gained from experience with other clients
    </li>
  </ul>

  <div class="corner-tile"></div>
  <span class="name-mark">Halvoran</span>
</section>

<section class="panel panel--back">
  <svg class="panel-shapes" viewBox="0 0 575 899" aria-hidden="true">
    <path d="M0 0 H575 V36 Q300 10 0 34Z" fill="var(--blue)"/>
    <path d="M0 34 Q300 10 575 36 V56 Q300 22 0 48Z" fill="#ffffff"/>
    <path d="M0 775 Q320 730 575 785 V899 H0Z" fill="#ffffff"/>
    <path d="M0 790 Q320 745 575 800 V899 H0Z" fill="var(--blue-deep)"/>
  </svg>

  <div class="round-frame frame-services"><div class="round-photo photo-team" role="img" aria-label="Photo of two businessmen reviewing a tablet"></div></div>
  <div class="round-frame frame-philosophy"><div class="round-photo photo-growth" role="img" aria-label="Illustration of rising financial charts held in open hands"></div></div>

  <h2 class="section-title back-title services-title">Services:</h2>
  <ul class="copy services-list">
    <li>Bookkeeping Controller Services Accounts Payable Management</li>
    <li>Account Receivable Management Check Writing Account Reconciliations</li>
    <li>Benchmarking Budgeting Financial Reports</li>
    <li>Financial Consulting Profit and Growth Consulting Financial Planning</li>
    <li>Succession &amp; Exit Planning Electronic Filing Cabinet Marketing Consulting</li>
  </ul>

  <h2 class="section-title back-title philosophy-title">Our Philosophy:</h2>
  <div class="copy philosophy-copy">
    <p>Accuracy – having strong financial systems in place that collect and measure all relevant data creates a compliant business and gives you a better understanding of your business.</p>
    <p>Understanding – Understanding what financial data is important and what it really means for your business will allow you to take appropriate actions to grow your business or to prevent future issues.</p>
    <p>Action – data in meaningless without action, however the right actions put you in control</p>
    <p>Control – When you take action based on accurate data that you understand, you are in complete control of your business and its future.</p>
  </div>

  <ul class="contact">
    <li><svg viewBox="0 0 12 12"><path d="M6 0a4 4 0 0 0-4 4c0 3 4 8 4 8s4-5 4-8a4 4 0 0 0-4-4zm0 5.6a1.6 1.6 0 1 1 0-3.2 1.6 1.6 0 0 1 0 3.2z"/></svg>48 Harbor Lane. Albany, NY, 12207. USA</li>
    <li><svg viewBox="0 0 12 12"><path d="M2.5 0.5l2 2.5-1 1.5c.8 1.6 2 2.8 3.5 3.5l1.5-1 2.5 2-1 2.5C5 11 1 7 0 1.5z"/></svg>(518) 555-0143</li>
    <li><svg viewBox="0 0 12 12"><path d="M0 2h12v8H0z M0 2l6 4.5L12 2" stroke="#2a2a2a" stroke-width=".8"/></svg>hello@halvoranbooks.com</li>
  </ul>

  <span class="web-address">www.halvoranbooks.com</span>

  <div class="corner-tile"></div>
  <span class="name-mark">Halvoran</span>
</section>

</body>
</html>
```